Business Card design for construction company

I would like a business card design for a construction company - Harlow Constructions. I have attached the ai logo file for use. I would like the card to be very smart and clean and incorporate only white and the two colours in the logo. I would like the card to have two sides. One side can just have the logo, the other with the relevant information.

Target Market(s)

Building and Construction Clients

Industry/Entity Type

Business

Contact Information for Business Card

Name: Tom Pardoe
Company: Harlow Constructions Pty Limited
Address: 14 Mallee Crescent Carrow Vale 2093
Phone: 0427 531 068
Email: tomp@harlowbuild-example.com.au

Font styles to use
Serif
Sans Serif

Requirements
Must have
• Details noted above
• Logo as provided
• Colours as in logo
• Square edges
• A font that compliments the logo
Should not have
• Any colour other than white and those in logo
• Rounded edges

```html
<!DOCTYPE html>
<html lang="en">
<head>
<meta charset="utf-8">
<title>Harlow Constructions – Business Card</title>
<link rel="stylesheet" href="https://fonts.googleapis.com/css2?family=Didact+Gothic&display=swap">
<style>
  :root {
    --slate: #4a545a;
    --sky: #5cc6e6;
    --paper: #ffffff;
    --backdrop: #e9eaeb;
  }
  * { margin: 0; padding: 0; box-sizing: border-box; }
  html, body {
    width: 1200px;
    height: 1200px;
    overflow: hidden;
    background: var(--backdrop);
    font-family: "Didact Gothic", sans-serif;
  }
  .sheet {
    position: relative;
    width: 1200px;
    height: 1200px;
  }
  .card {
    position: absolute;
    left: 150px;
    width: 900px;
    height: 514px;
    background: var(--paper);
    overflow: hidden;
    box-shadow: 0 2px 10px rgba(0, 0, 0, 0.12);
  }
  .card--front { top: 70px; }
  .card--back { top: 616px; }

  /* Front */
  .front__name {
    position: absolute;
    left: 0;
    right: 0;
    top: 200px;
    text-align: center;
    color: var(--slate);
    font-size: 40px;
    letter-spacing: 6px;
    text-transform: uppercase;
  }
  .front__rule {
    position: absolute;
    left: 300px;
    right: 0;
    top: 424px;
    height: 3px;
    background: var(--sky);
  }
  .front__band {
    position: absolute;
    left: 0;
    right: 0;
    bottom: 0;
    height: 48px;
    background: var(--slate);
  }

  /* Back */
  .back__header {
    position: absolute;
    left: 0;
    right: 0;
    top: 0;
    height: 230px;
    background: var(--paper);
  }
  .back__name-mark {
    position: absolute;
    left: 60px;
    top: 128px;
    color: var(--slate);
    font-size: 24px;
    letter-spacing: 4px;
    text-transform: uppercase;
  }
  .back__mark-rule {
    position: absolute;
    left: 60px;
    top: 170px;
    width: 300px;
    height: 3px;
    background: var(--sky);
  }
  .back__body {
    position: absolute;
    left: 0;
    right: 0;
    top: 230px;
    bottom: 0;
    background: var(--slate);
    color: var(--paper);
  }
  .back__person {
    position: absolute;
    left: 0;
    right: 0;
    top: 38px;
    text-align: center;
    font-size: 36px;
  }
  .back__contact {
    position: absolute;
    right: 40px;
    top: 96px;
    text-align: right;
    font-size: 22px;
    line-height: 34px;
  }
  .back__contact-rule {
    position: absolute;
    left: 470px;
    right: 40px;
    top: 172px;
    height: 2px;
    background: var(--paper);
  }
  .back__address {
    position: absolute;
    left: 60px;
    top: 150px;
    font-size: 22px;
    line-height: 32px;
  }
  .back__base-rule {
    position: absolute;
    left: 0;
    right: 0;
    top: 242px;
    height: 2px;
    background: var(--paper);
  }
</style>
</head>
<body>
  <main class="sheet">
    <section class="card card--front" aria-label="Card front">
      <div class="front__name">Harlow Constructions</div>
      <div class="front__rule"></div>
      <div class="front__band"></div>
    </section>

    <section class="card card--back" aria-label="Card back">
      <div class="back__header">
        <div class="back__name-mark">Harlow Constructions</div>
        <div class="back__mark-rule"></div>
      </div>
      <div class="back__body">
        <div class="back__person">Tom Pardoe</div>
        <div class="back__contact">
          <div class="back__phone">0427 531 068</div>
          <div class="back__email">tomp@harlowbuild-example.com.au</div>
        </div>
        <div class="back__contact-rule"></div>
        <address class="back__address" style="font-style: normal;">
          <div>14 Mallee Crescent</div>
          <div>Carrow Vale 2093</div>
        </address>
        <div class="back__base-rule"></div>
      </div>
    </section>
  </main>
</body>
</html>
```